Copperline Business Management Business Card Design Project

I have a new business called Copperline Business Management Limited. We provide business services for the UK for areas which include

Mentoring / Coaching
Interim Management
Non Executive Director / Chairman placement
Angel Investment support
Merger & Acquisition advice
Selling your business advice

I would like a background colour on the logo, a logo and our company name on the logo if possible.

I am open to colours but we want to portray a strong safe business with credibility

The business card design must match that of the logo design
Updates

Target Market(s)

SME and Medium size businesses with the owners, MD's, CEO or senior management as the target audiabce

Industry/Entity Type

Business

Requirements
Must have
• Match the logo design.
Look professional and quality
Should not have
• Old style text and colours
Poor logos depicting money

```html
<!DOCTYPE html>
<html lang="en">
<head>
<meta charset="utf-8">
<title>Copperline Business Management Limited – Business Card</title>
<link rel="stylesheet" href="https://fonts.googleapis.com/css2?family=Open+Sans:wght@400;500&display=swap">
<style>
  :root {
    --stage: #e9e7e4;
    --card: #ffffff;
    --ink: #111111;
    --accent: #e3161b;
    --rule: #222222;
    --shadow: rgba(0, 0, 0, 0.18);
  }
  * { box-sizing: border-box; margin: 0; padding: 0; }
  html, body {
    width: 1200px;
    height: 900px;
    overflow: hidden;
    background: var(--stage);
    font-family: "Open Sans", "Lucida Sans", sans-serif;
    color: var(--ink);
  }
  .business-card {
    position: absolute;
    left: 100px;
    top: 160px;
    width: 1000px;
    height: 580px;
    background: var(--card);
    box-shadow: 0 10px 30px var(--shadow);
    overflow: hidden;
  }
  .brand {
    position: absolute;
    right: 40px;
    top: 34px;
    display: flex;
    flex-direction: column;
    align-items: flex-end;
    gap: 18px;
  }
  .brand-mark {
    width: 58px;
    height: 58px;
    background: var(--accent);
    margin-right: 20px;
  }
  .brand-name {
    font-size: 22px;
    font-weight: 400;
    letter-spacing: 0.6px;
    color: var(--ink);
  }
  .divider {
    position: absolute;
    left: 0;
    right: 0;
    top: 340px;
    height: 1.5px;
    background: var(--rule);
  }
  .holder-name {
    position: absolute;
    left: 40px;
    top: 290px;
    font-size: 31px;
    font-weight: 400;
    letter-spacing: 0.8px;
    color: var(--accent);
  }
  .holder-title {
    position: absolute;
    left: 40px;
    top: 350px;
    font-size: 20px;
    letter-spacing: 0.5px;
  }
  .address {
    position: absolute;
    left: 40px;
    bottom: 46px;
    font-size: 22px;
    line-height: 26px;
    letter-spacing: 0.5px;
    font-style: normal;
  }
  .phones {
    position: absolute;
    right: 40px;
    bottom: 70px;
    font-size: 24px;
    line-height: 26px;
    letter-spacing: 1px;
    list-style: none;
  }
  .base-band {
    position: absolute;
    left: 0;
    right: 0;
    bottom: 0;
    height: 30px;
    background: var(--accent);
  }
</style>
</head>
<body>
  <article class="business-card">
    <header class="brand">
      <span class="brand-mark" aria-hidden="true"></span>
      <span class="brand-name">Copperline Business Management Limited</span>
    </header>

    <h1 class="holder-name">Sample Name</h1>
    <div class="divider" aria-hidden="true"></div>
    <p class="holder-title">CEO</p>

    <address class="address">
      Sample Address<br>
      Sample Street<br>
      yourname@sample.com
    </address>

    <ul class="phones">
      <li>P: 111-222-333</li>
      <li>M: 555-444-333</li>
    </ul>

    <div class="base-band" aria-hidden="true"></div>
  </article>
</body>
</html>
```